Freelance film producer/editor wants you to brisk vanta!

'Brisk Vanta' is my production business based in Melbourne, though I do a fair bit of work overseas. I'm a one woman show most of the time but enlist other crew members for larger projects. I manage productions from start to finish including producing, filming, editing, distribution, photography and animation.

My current tag line and details are as follows:

Greta Hollensby
Producer. Editor. Thinker.
[M] +61 417 562 093
[E] gh[at]briskvanta.com.au
www.briskvanta.com.au

I have a fairly wicked sense of humour and love a good pun, so feel free to work this into your design!

The final designs should demonstrate the areas I work in but not limited to. I'd rather not use old and typical "film" looking elements such as a clapper or negative reel. Having said that, the logo itself (attached) is quite typical because the first 'o' is a closed aperture and the second is a wide aperture. Happy for the logo to be pulled apart for the business card to be more interesting.

The majority of projects I work on are quite different and in some cases a bit crazy. Lots of travel involved. The main difference between me and other producers is that I don't say I work in 'film', even though i do. I want the card to leave me open to new roles and projects as opposed to squashing myself into one particular category.

I'm open to colour but prefer a simple design that isn't too hectic.

I have also attached an example I did like that was printed on plastic but then I realised so many other people had ripped it off....

I'm open to paper board or plastic (transparent) designs etc. One sided or two sided.

Thanks for sharing your ideas with me and please, go as nuts as you want to with this! :)

Target Market(s)

My clients range from non profits in health and educational institutions to record labels and well known artists. The business attracts corporates as well though the majority of my business is achieved through referral and word of mouth so most people will soon realise that my personality and work are very much intertwined and the reason they hire me for a job.

Industry/Entity Type

Business

Font styles to use
Other font styles liked:
• Eurostile or similar

Requirements
Must have
• I have a very open mind when it comes to design. I do like the existing tag line but if you can come up with something better I'm all ears! (and eyes)

Nice to have
• Back of the business card can be graphics, there can be transparent elements or holes, embossing options...
Should not have
• Besides my name, nothing should scream "I am woman!" because in my industry that's not a selling point.

The colour pink is a definite no.

```html
<!DOCTYPE html>
<html lang="en">
<head>
<meta charset="utf-8">
<title>Brisk Vanta – Business Card</title>
<link rel="stylesheet" href="https://fonts.googleapis.com/css2?family=Montserrat:wght@300;600;700&display=swap">
<style>
  :root {
    --backdrop: #6b5a48;
    --card-tint: rgba(246, 236, 210, 0.78);
    --card-edge: rgba(255, 250, 236, 0.55);
    --mark: #221f1e;
    --ink: #1f1c1b;
    --ink-soft: #2a2624;
  }
  * { margin: 0; padding: 0; box-sizing: border-box; }
  html, body {
    width: 1200px;
    height: 1034px;
    overflow: hidden;
  }
  body {
    background: var(--backdrop);
    font-family: "Montserrat", Arial, sans-serif;
    color: var(--ink);
    position: relative;
  }
  .card {
    position: absolute;
    left: 398px;
    top: 167px;
    width: 402px;
    height: 702px;
    background: var(--card-tint);
    border: 1px solid var(--card-edge);
    box-shadow: inset 0 0 0 1px rgba(255, 255, 255, 0.18);
  }
  .brand-disc {
    position: absolute;
    left: 64px;
    top: 61px;
    width: 274px;
    height: 274px;
    border-radius: 50%;
    background: var(--mark);
  }
  .wordmark {
    position: absolute;
    right: 29px;
    top: 408px;
    font-weight: 300;
    font-size: 46px;
    line-height: 56px;
    letter-spacing: 0.3px;
    color: var(--ink);
    white-space: nowrap;
  }
  .holder {
    position: absolute;
    right: 29px;
    top: 518px;
    text-align: right;
  }
  .holder-name {
    font-weight: 700;
    font-size: 26px;
    letter-spacing: -0.5px;
    line-height: 1;
    white-space: nowrap;
  }
  .holder-role {
    margin-top: 11px;
    font-weight: 600;
    font-size: 15px;
    color: var(--ink-soft);
  }
  .contact {
    position: absolute;
    right: 29px;
    top: 602px;
    text-align: right;
    font-weight: 600;
    font-size: 15.5px;
    line-height: 25px;
    color: var(--ink-soft);
    white-space: nowrap;
  }
</style>
</head>
<body>
  <main class="card">
    <div class="brand-disc" role="img" aria-label="Brisk Vanta brand mark area"></div>
    <div class="wordmark">brisk vanta</div>
    <div class="holder">
      <h1 class="holder-name">GRETA HOLLENSBY</h1>
      <p class="holder-role">Producer.Editor.Thinker</p>
    </div>
    <div class="contact">
      <p class="contact-line">+61 417 562 093 • gh@briskvanta.com.au</p>
      <p class="contact-line">www.briskvanta.com.au</p>
    </div>
  </main>
</body>
</html>
```